Commercial Refrigeration Service Company requires stylish and fresh looking flyer.

We need a flyer to hand out to new customers. It should have a photo and our branding, list all the services that are offered and our contact details.
We would like two flyers to be supplied, both identical though one offering a discount until July ( Half Price Service Fee ). The flyer should be clear, interesting and in similar colours to the branding package supplied.
Please look at our website for information about the services on offer:
www.brambo-cooling.com.au

Target Market(s)

Cafes, bars, restaurants, pubs ect.

Font styles to use
Other font styles liked:
• Font package provided

Colors
85cae6
ffffff
333333

Requirements
Must have
• - The photo provided.
• - The company logo.
• - Similar feel to the website & business card.
• - Smooth layout and clear to understand.
Should not have
• - No clunky badges or prints.

```html
<!DOCTYPE html>
<html lang="en">
<head>
<meta charset="utf-8">
<title>Brambo Cooling – Flyer</title>
<link href="https://fonts.googleapis.com/css2?family=Ubuntu:wght@300;400;500&display=swap" rel="stylesheet">
<style>
  :root{
    --brand-blue:#85cae6;
    --accent-blue:#1d9ad6;
    --banner-dark:#2a86b8;
    --banner-light:#3aa8da;
    --ink:#333333;
    --white:#ffffff;
    --panel:#f3f3f3;
    --panel-line:#c9c9c9;
    --icon-grey:#9a9a9a;
    --page:#e4e4e4;
  }
  *{margin:0;padding:0;box-sizing:border-box}
  html,body{width:1200px;height:1200px;overflow:hidden}
  body{background:var(--page);font-family:"Ubuntu",sans-serif;color:var(--ink);position:relative}
  .flyer{position:absolute;left:152px;top:20px;width:920px;height:1191px;background:var(--white);
    transform:scale(0.974);transform-origin:0 0;overflow:hidden;box-shadow:0 2px 10px rgba(0,0,0,.15)}
  .hero-photo{position:absolute;left:0;top:0;width:920px;height:545px;
    background:linear-gradient(180deg,#c4dbea 0%,#e8eff3 34%,#8fb3c6 44%,#cfcac0 54%,#6b717b 72%,#8d8d8b 100%)}
  .brand-box{position:absolute;left:43px;top:40px;width:309px;height:136px;background:var(--brand-blue);
    display:flex;flex-direction:column;align-items:center;justify-content:center;gap:6px}
  .brand-name{font-weight:400;color:var(--ink);letter-spacing:12px;font-size:30px;line-height:1;padding-left:12px}
  .brand-name.small{font-size:16px;letter-spacing:8px;padding-left:8px}
  .registration{position:absolute;right:50px;top:44px;text-align:left;font-size:22px;line-height:29px;font-weight:300}
  .registration .label{color:var(--accent-blue);font-weight:400}
  .service-banner{position:absolute;left:0;top:545px;width:920px;height:100px;
    background:linear-gradient(90deg,var(--banner-dark),var(--banner-light));color:var(--white);padding:20px 0 0 41px}
  .service-banner .line1{font-size:26px;font-weight:300;letter-spacing:-.3px}
  .service-banner .line1 b{font-weight:500}
  .service-banner .line2{font-size:28px;font-weight:300;margin-top:4px}
  .starburst{position:absolute;left:700px;top:492px;width:168px;height:168px}
  .starburst span{position:absolute;left:14px;top:14px;width:140px;height:140px;background:#4a4a4a}
  .starburst span:nth-child(2){transform:rotate(15deg)}
  .starburst span:nth-child(3){transform:rotate(30deg)}
  .starburst span:nth-child(4){transform:rotate(45deg)}
  .starburst span:nth-child(5){transform:rotate(60deg)}
  .starburst span:nth-child(6){transform:rotate(75deg)}
  .starburst p{position:absolute;inset:0;display:flex;align-items:center;justify-content:center;text-align:center;
    color:var(--white);font-size:19px;line-height:25px}
  .welcome{position:absolute;left:43px;top:652px;width:834px}
  .welcome h2{font-size:20px;font-weight:400}
  .welcome h2 span{color:var(--accent-blue)}
  .welcome p{font-size:11.6px;font-weight:300;line-height:16.4px;text-align:justify;margin-top:8px}
  .services{position:absolute;left:43px;top:768px;width:834px;height:361px;background:var(--panel);
    border:1px solid var(--panel-line);border-radius:8px}
  .services-title{position:absolute;left:50%;top:-13px;transform:translateX(-50%);background:var(--white);
    padding:0 6px;font-size:20px;font-weight:400;white-space:nowrap}
  .services-title span{color:var(--accent-blue)}
  .service{position:absolute;width:200px;margin-left:-100px;text-align:center}
  .service .icon{width:50px;height:50px;border-radius:50%;background:var(--icon-grey);margin:0 auto;
    box-shadow:0 4px 4px rgba(0,0,0,.12);display:flex;align-items:center;justify-content:center}
  .service h3{font-size:14px;font-weight:400;color:var(--accent-blue);margin-top:12px}
  .service p{font-size:11.6px;font-weight:300;line-height:16.4px;margin-top:4px}
  .contact-bar{position:absolute;left:0;top:1133px;width:920px;height:45px;background:#333}
  .contact-bar .blue{position:absolute;left:0;top:0;height:45px;width:715px;background:var(--accent-blue);
    clip-path:polygon(0 0,100% 0,95% 100%,0 100%)}
  .contact-bar .info{position:absolute;left:40px;top:0;height:45px;display:flex;align-items:center;gap:20px;
    color:var(--white);font-size:12.5px;font-weight:300}
  .contact-bar .info span{display:flex;align-items:center;gap:6px}
  .contact-bar .phone{position:absolute;right:42px;top:0;height:45px;display:flex;align-items:center;gap:10px;
    color:var(--white);font-size:20px}
</style>
</head>
<body>
<main class="flyer">
  <div class="hero-photo" role="img" aria-label="Photo of the technician standing beside the company service ute at a beachside car park"></div>

  <div class="brand-box">
    <div class="brand-name">BRAMBO</div>
    <div class="brand-name small">COOLING</div>
  </div>

  <div class="registration">
    <div><span class="label">ABN:</span> 48 207 913 552</div>
    <div><span class="label">Licence No:</span> 517283B</div>
  </div>

  <section class="service-banner">
    <div class="line1"><b>COMMERCIAL</b> REFRIGERATION &amp; <b>ELECTRICAL</b> SERVICES.</div>
    <div class="line2">Ice makers &amp; beer systems</div>
  </section>

  <div class="starburst">
    <span></span><span></span><span></span><span></span><span></span><span></span>
    <p>24 Hr Service,<br>Sales &amp;<br>Installations</p>
  </div>

  <section class="welcome">
    <h2>Welcome To <span>Brambo Cooling</span></h2>
    <p>Sam and his team believe in developing tight relationships with their clients and keeping things simple by offering a personalised service – speak to the same people and see the same faces. Brambo is completely paperless and uses cloud based trade service software to build a complete profile of your venue and equipment, allowing Sam to offer tailored advice for your business.<br>
    Receive a text message when a technician is on their way &amp; your invoice straight to your email at time of service. Pay with card, cash or cheque on site or online.</p>
  </section>

  <section class="services">
    <div class="services-title">OUR <span>SERVICES</span></div>

    <div class="service" style="left:100px;top:20px">
      <div class="icon"><svg width="26" height="30" viewBox="0 0 26 30" fill="none" stroke="#fff" stroke-width="1.6"><rect x="10" y="2" width="6" height="18" rx="3"/><circle cx="13" cy="24" r="4.5"/><path d="M18 6h4M18 10h3M18 14h4"/></svg></div>
      <h3>Commercial Refrigeration</h3>
      <p>Cool rooms, freezer rooms undercounter systems,self-contained fridges/freezers, display fridges, butcher's cases, etc.</p>
    </div>
    <div class="service" style="left:315px;top:20px">
      <div class="icon"><svg width="26" height="30" viewBox="0 0 26 30" fill="none" stroke="#fff" stroke-width="1.6"><path d="M4 4h18l-2 22H6z"/><path d="M6 11h14"/><rect x="9" y="14" width="4" height="4"/><rect x="13" y="18" width="4" height="4"/></svg></div>
      <h3>Ice makers</h3>
      <p>Cubers and flakers of all major brands. Undercounter to larger commercial systems. Service, maintenance and installations.</p>
    </div>
    <div class="service" style="left:515px;top:20px">
      <div class="icon"><svg width="28" height="30" viewBox="0 0 28 30" fill="none" stroke="#fff" stroke-width="1.6"><path d="M6 10h10v6H6z"/><path d="M16 12h6v8"/><path d="M10 10V4l8-2"/><path d="M8 20h8v8H8z"/></svg></div>
      <h3>Beer Systems</h3>
      <p>Glycol systems, beer plumbing, CO2 monitors, gas boards and self-contained undercounter beer systems.</p>
    </div>
    <div class="service" style="left:722px;top:20px">
      <div class="icon"><svg width="24" height="30" viewBox="0 0 24 30" fill="none" stroke="#fff" stroke-width="1.6" stroke-linejoin="round"><path d="M14 2L5 17h7l-3 11 10-16h-7z"/></svg></div>
      <h3>Electrical</h3>
      <p>New Installations, alterations and upgrades. LED lighting systems, power circuit repairs, switch boards, air curtains &amp; outdoor heating installations.</p>
    </div>

    <div class="service" style="left:192px;top:190px">
      <div class="icon"><svg width="28" height="28" viewBox="0 0 28 28" fill="none" stroke="#fff" stroke-width="1.6" stroke-linecap="round"><path d="M5 23L17 11"/><circle cx="20" cy="8" r="4"/><path d="M5 5l18 18"/><path d="M3 7l4-4"/></svg></div>
      <h3>24hr Service</h3>
      <p>Service, repairs and maintenance. An emergency after-hours service is also provided.</p>
    </div>
    <div class="service" style="left:417px;top:190px">
      <div class="icon"><svg width="28" height="28" viewBox="0 0 28 28" fill="none" stroke="#fff" stroke-width="1.6" stroke-linejoin="round"><path d="M2 5h4l3 13h14l2-9H8"/><circle cx="11" cy="22" r="2"/><circle cx="21" cy="22" r="2"/></svg></div>
      <h3>Sales</h3>
      <p>Commercial refrigeration, icemakers &amp; beer equipment. Electrical equipment including lighting, switchboards and heating. A variety of brands to suit any budget.</p>
    </div>
    <div class="service" style="left:630px;top:190px">
      <div class="icon"><svg width="28" height="28" viewBox="0 0 28 28" fill="none" stroke="#fff" stroke-width="1.6" stroke-linecap="round"><path d="M5 5l18 18M23 5L5 23"/><path d="M3 9l6-6M19 25l6-6"/></svg></div>
      <h3>Installations</h3>
      <p>Cool rooms, freezer rooms, under benches, ice machines, cellar fit-outs, glycol systems, undercounter beer systems, lighting, power, outdoor heating, etc</p>
    </div>
  </section>

  <footer class="contact-bar">
    <div class="blue"></div>
    <div class="info">
      <span><svg width="10" height="14" viewBox="0 0 10 14"><path d="M5 0a5 5 0 0 1 5 5c0 4-5 9-5 9S0 9 0 5a5 5 0 0 1 5-5z" fill="#fff"/><circle cx="5" cy="5" r="2" fill="#1d9ad6"/></svg>PO Box 1184 Seabright, NSW 2099</span>
      <span><svg width="14" height="10" viewBox="0 0 14 10" fill="none" stroke="#fff" stroke-width="1.3"><rect x=".7" y=".7" width="12.6" height="8.6"/><path d="M.7 .7L7 6l6.3-5.3"/></svg>info@brambo-cooling.com.au</span>
      <span><svg width="14" height="14" viewBox="0 0 14 14" fill="none" stroke="#fff" stroke-width="1.2"><circle cx="7" cy="7" r="6"/><ellipse cx="7" cy="7" rx="2.6" ry="6"/><path d="M1 7h12"/></svg>www.brambo-cooling.com.au</span>
    </div>
    <div class="phone"><svg width="16" height="16" viewBox="0 0 16 16" fill="none" stroke="#85cae6" stroke-width="1.5" stroke-linejoin="round"><path d="M3 1l3 3-2 2c1 2 4 5 6 6l2-2 3 3-2 2C7 15 1 9 1 3z"/></svg>0400 512 870</div>
  </footer>
</main>
</body>
</html>
```